Lantern Hill Publicity is a new boutique Press Office with a small roster of well-chosen clients across an array of disciplines; from Art and Technology to Restaurants and Fashion. Based in Greenpoint Brooklyn, Lantern Hill Publicity achieves outstanding results through hard work, tenacity, efficiency and a sense of humor. We need a simple, versatile and classic design. We would like each side of the card to be white text on a black background.

Boutique

```html
<!DOCTYPE html>
<html lang="en">
<head>
<meta charset="utf-8">
<title>Lantern Hill Publicity — Business Card</title>
<link rel="stylesheet" href="https://fonts.googleapis.com/css2?family=Playfair+Display:wght@400;700&display=swap">
<style>
  :root {
    --stage: #e4e5e7;
    --card: #141517;
    --ink: #ffffff;
    --ink-soft: #c9cacc;
    --serif: "Playfair Display", Georgia, serif;
  }
  * { margin: 0; padding: 0; box-sizing: border-box; }
  html, body {
    width: 1200px; height: 900px; overflow: hidden;
    background: var(--stage);
  }
  .stage {
    width: 1200px; height: 900px;
    display: flex; flex-direction: column;
    align-items: center; justify-content: center; gap: 60px;
  }
  .card {
    width: 630px; height: 360px;
    background: var(--card);
    color: var(--ink);
    font-family: var(--serif);
    position: relative;
    display: flex; flex-direction: column; align-items: center;
  }
  .wordmark {
    font-weight: 400;
    text-transform: uppercase;
    letter-spacing: 0.22em;
    color: var(--ink);
    text-align: center;
    white-space: nowrap;
  }
  /* Contact side */
  .card--contact .wordmark { font-size: 24px; margin-top: 92px; }
  .person { margin-top: 46px; text-align: center; }
  .person__name { font-size: 24px; font-weight: 700; }
  .person__role { font-size: 12px; color: var(--ink-soft); margin-top: 2px; }
  .contacts {
    position: absolute; bottom: 40px; left: 0; right: 0;
    display: flex; justify-content: center; gap: 34px;
    font-size: 12px; color: var(--ink-soft);
  }
  .contact { display: flex; align-items: center; gap: 8px; }
  .contact svg { width: 13px; height: 13px; fill: var(--ink); }
  /* Address side */
  .card--address { justify-content: center; }
  .card--address .wordmark { font-size: 32px; margin-top: -20px; }
  .address { font-size: 16px; color: var(--ink-soft); margin-top: 44px; letter-spacing: 0.02em; }
</style>
</head>
<body>
<main class="stage">
  <section class="card card--contact" aria-label="Card front">
    <h1 class="wordmark">Lantern Hill Publicity</h1>
    <div class="person">
      <p class="person__name">Mara Quinlan</p>
      <p class="person__role">Director</p>
    </div>
    <ul class="contacts" style="list-style:none">
      <li class="contact">
        <svg viewBox="0 0 16 16" aria-hidden="true"><rect x="4" y="1" width="8" height="14" rx="1.5"/><rect x="5.5" y="3" width="5" height="8" fill="#141517"/></svg>
        +12 555 0190
      </li>
      <li class="contact">
        <svg viewBox="0 0 16 16" aria-hidden="true"><path d="M1 3h14v10H1z"/><path d="M1.5 3.5 8 9l6.5-5.5" stroke="#141517" stroke-width="1.3" fill="none"/></svg>
        info@lhpub.com
      </li>
      <li class="contact">
        <svg viewBox="0 0 16 16" aria-hidden="true"><circle cx="8" cy="8" r="7"/><g stroke="#141517" stroke-width="1" fill="none"><ellipse cx="8" cy="8" rx="3" ry="6.5"/><path d="M1.5 8h13M2.5 5h11M2.5 11h11"/></g></svg>
        www.lhpub.com
      </li>
    </ul>
  </section>

  <section class="card card--address" aria-label="Card back">
    <h2 class="wordmark">Lantern Hill Publicity</h2>
    <p class="address">48 Harbor Row, Greenpoint, Brooklyn</p>
  </section>
</main>
</body>
</html>
```